Calderwyn Structural Roof Inc.

We need a business card design for a commercial roofing company metro Boston based. We are a roofing company that help people manage buildings and build relationships with clients. We would like a unique card that stands out. We want a business card with a white background. We do not want a roof as the logo.

Industry/Entity Type

Roofing

```html
<!DOCTYPE html>
<html lang="en">
<head>
<meta charset="UTF-8">
<title>Calderwyn Structural Roof Inc. — Business Card</title>
<link href="https://fonts.googleapis.com/css2?family=Jost:wght@500;600;700&display=swap" rel="stylesheet">
<style>
  :root {
    --brand-blue: #21409a;
    --ink-brown: #2e1408;
    --card-white: #ffffff;
    --backdrop: #e6e7ea;
  }
  * { margin: 0; padding: 0; box-sizing: border-box; }
  html, body { width: 1200px; height: 800px; overflow: hidden; }
  body {
    background: var(--backdrop);
    font-family: "Jost", "Trebuchet MS", sans-serif;
    display: flex;
    align-items: center;
    justify-content: center;
    gap: 40px;
  }
  .card {
    width: 540px;
    height: 309px;
    position: relative;
    overflow: hidden;
    box-shadow: 0 6px 18px rgba(0,0,0,0.18);
  }

  /* Front */
  .card-front {
    background: var(--brand-blue);
    color: var(--card-white);
  }
  .front-name {
    position: absolute;
    left: 0; right: 0; top: 98px;
    text-align: center;
    font-weight: 700;
    font-size: 30px;
    line-height: 1.2;
    letter-spacing: 0.5px;
  }
  .front-name .mark-square {
    display: inline-block;
    width: 18px; height: 18px;
    background: var(--card-white);
    margin-right: 12px;
    vertical-align: 1px;
  }
  .front-address {
    position: absolute;
    left: 0; right: 0; top: 200px;
    text-align: center;
    font-weight: 600;
    font-size: 15px;
  }

  /* Back */
  .card-back { background: var(--card-white); }
  .back-band {
    position: absolute;
    left: 0; right: 0; bottom: 0;
    height: 46px;
    background: var(--brand-blue);
  }
  .contacts {
    position: absolute;
    left: 34px; top: 34px;
  }
  .contact { margin-bottom: 22px; }
  .contact-name {
    color: var(--brand-blue);
    font-weight: 700;
    font-size: 16px;
    letter-spacing: 0.5px;
    text-transform: uppercase;
  }
  .contact-title {
    color: var(--ink-brown);
    font-weight: 600;
    font-size: 14px;
    margin-bottom: 6px;
  }
  .contact-line {
    display: flex;
    font-size: 14px;
    line-height: 1.3;
  }
  .contact-label {
    width: 68px;
    color: var(--brand-blue);
    font-weight: 600;
  }
  .contact-value { color: var(--ink-brown); font-weight: 500; }

  .back-brand {
    position: absolute;
    right: 30px; top: 96px;
    width: 210px;
    text-align: center;
    color: var(--brand-blue);
  }
  .back-brand-name {
    font-weight: 700;
    font-size: 22px;
    line-height: 1.15;
    margin-bottom: 14px;
  }
  .back-web, .back-phone {
    font-weight: 700;
    font-size: 16px;
    line-height: 1.3;
  }
</style>
</head>
<body>
  <section class="card card-front">
    <div class="front-name"><span class="mark-square"></span>Calderwyn<br>Structural Roof Inc.</div>
    <div class="front-address">42 Harbor Mill Rd. Quincy, Ma. 02169-0000</div>
  </section>

  <section class="card card-back">
    <div class="contacts">
      <div class="contact">
        <div class="contact-name">Marco Estevan</div>
        <div class="contact-title">President</div>
        <div class="contact-line"><span class="contact-label">E-mail :</span><span class="contact-value">marco@calderwynroof.com</span></div>
        <div class="contact-line"><span class="contact-label">Direct :</span><span class="contact-value">617-555-0148</span></div>
      </div>
      <div class="contact">
        <div class="contact-name">Dean Callister</div>
        <div class="contact-line"><span class="contact-label">E-mail :</span><span class="contact-value">dean@calderwynroof.com</span></div>
        <div class="contact-line"><span class="contact-label">Direct :</span><span class="contact-value">617-555-0148</span></div>
      </div>
    </div>
    <div class="back-brand">
      <div class="back-brand-name">Calderwyn</div>
      <div class="back-web">www.calderwynroof.com</div>
      <div class="back-phone">617-555-0148</div>
    </div>
    <div class="back-band"></div>
  </section>
</body>
</html>
```